pharmacy bi or tri -fold brochure for 3 pharmacy's

we are looking to promote our pharmacy specialty services, specifically the outreach (or mobile services) services such as daily witness of medication ingestion, in home diabetes program, blood pressure and glucose monitoring, customizing medications into powders and liquids so that they are easier to take, free mobile hearing tests, mobile compression sock and brace fitting. see attached brochure from our competitors. we want something more modern/fresh with images of patients at home being serviced. we will need to tweek the content fro our competitor's . our website is www. brightwell pharmacy.ca which lists our 3 pharmacy locations, our logo etc.

Font styles to use
Sans Serif

Colors
85cae6
0255a3
fbee3f
ffffff

Requirements
Must have
• 8.5" x 11" with consistent color scheme to our website www.brightwellphamacy.ca

```html
<!DOCTYPE html>
<html lang="en">
<head>
<meta charset="utf-8">
<title>Specialized Services – Pharmacy at Home Program</title>
<link rel="stylesheet" href="https://fonts.googleapis.com/css2?family=Questrial&family=Arimo:ital,wght@0,400;0,700;1,400;1,700&display=swap">
<style>
  :root {
    --navy: #0a358a;
    --navy-deep: #062c78;
    --sky: #4fc3f0;
    --sky-strip: #3fb2e8;
    --orange: #f15a24;
    --ink: #2b2b2b;
    --head-blue: #1b3f95;
    --rule: #dcdcdc;
    --white: #ffffff;
    --page: #ffffff;
  }
  * { box-sizing: border-box; margin: 0; padding: 0; }
  html, body { width: 1200px; height: 1000px; overflow: hidden; background: var(--page); }
  body { position: relative; font-family: "Arimo", Arial, sans-serif; }

  .brochure {
    position: absolute; left: 10px; top: 35px; width: 1178px; height: 908px;
    background: var(--navy);
    box-shadow: 0 6px 10px rgba(0,0,0,.25);
  }
  .accent-strip { position: absolute; left: 0; top: 0; width: 12px; height: 908px; background: var(--sky-strip); }

  /* Left panel */
  .services { position: absolute; left: 12px; top: 0; width: 576px; height: 908px; color: var(--white); }
  .services-title {
    position: absolute; left: 27px; top: 22px;
    font-family: "Questrial", sans-serif; font-size: 23px; color: var(--sky); letter-spacing: .2px;
  }
  .services-sub { position: absolute; left: 27px; top: 59px; font-size: 16.5px; font-style: italic; }
  .service { position: absolute; left: 30px; display: flex; align-items: flex-start; gap: 0; font-size: 17px; line-height: 22px; }
  .service .icon { width: 40px; height: 36px; flex: none; margin-top: -6px; }
  .service .label { margin-left: 22px; }
  .sub-list { list-style: none; margin-top: 4px; }
  .sub-list li { display: flex; align-items: center; gap: 8px; height: 27px; margin-left: -8px; }
  .tick { width: 18px; height: 18px; flex: none; }

  .more-title { position: absolute; left: 32px; top: 584px; font-size: 17px; font-weight: 700; font-style: italic; }
  .extra { position: absolute; left: 0; display: flex; align-items: center; font-size: 17px; line-height: 22px; }
  .extra .thumb {
    width: 83px; height: 56px; flex: none;
    clip-path: polygon(0 0, 85% 0, 100% 50%, 85% 100%, 0 100%);
  }
  .extra .label { margin-left: 9px; }

  /* Right panel */
  .house-calls { position: absolute; left: 588px; top: 0; width: 588px; height: 893px; background: var(--white); color: var(--ink); }
  .hero {
    position: absolute; left: 0; top: 0; width: 588px; height: 203px;
    background: linear-gradient(100deg, #e9e4dc 0%, #cfc6ba 35%, #3f7fa6 48%, #f0ece6 66%, #ddd5c9 100%);
  }
  .hc-title { position: absolute; left: 40px; top: 213px; font-family: "Questrial", sans-serif; font-size: 22.5px; color: var(--head-blue); letter-spacing: .3px; }
  .hc-program { position: absolute; left: 40px; top: 242px; font-family: "Questrial", sans-serif; font-size: 19px; color: var(--head-blue); }
  .hc-freq { position: absolute; left: 40px; top: 266px; font-size: 16px; }
  .hc-freq em { font-size: 13px; }

  .step { position: absolute; left: 42px; width: 488px; display: flex; align-items: center; font-size: 16.5px; line-height: 21px; border-bottom: 1px solid var(--rule); }
  .step .icon { width: 46px; height: 40px; flex: none; }
  .step .label { margin-left: 18px; }
  .step.plain { border-bottom: none; }

  .daily-title { position: absolute; left: 48px; top: 530px; font-size: 16.5px; font-weight: 700; font-style: italic; }
  .daily-list { position: absolute; left: 78px; top: 554px; list-style: none; font-size: 16px; }
  .daily-list li { display: flex; align-items: center; gap: 4px; height: 27px; letter-spacing: -.2px; }
  .footnote { position: absolute; left: 110px; top: 863px; font-size: 13px; font-style: italic; }
</style>
</head>
<body>
<div class="brochure">
  <div class="accent-strip"></div>

  <section class="services">
    <h2 class="services-title">CHECK OUT OUR SPECIALIZED SERVICES:</h2>
    <p class="services-sub">Check out our Specialized Services:</p>

    <div class="service" style="top:108px">
      <svg class="icon" viewBox="0 0 40 36"><path d="M22 4c-7 0-11 5-11 11 0 4 3 6 3 10 0 4 3 7 7 6 3-1 3-4 5-6 3-3 6-6 6-11 0-6-4-10-10-10z" fill="none" stroke="#f15a24" stroke-width="3"/><circle cx="21" cy="15" r="3" fill="#f15a24"/></svg>
      <span class="label">Hearing Aid Testing &amp; Fitting (at pharmacy or at home)</span>
    </div>
    <div class="service" style="top:146px">
      <svg class="icon" viewBox="0 0 40 36"><rect x="8" y="2" width="24" height="32" rx="3" fill="#f15a24"/><g fill="#fff"><circle cx="15" cy="10" r="3"/><circle cx="25" cy="10" r="3"/><circle cx="15" cy="18" r="3"/><circle cx="25" cy="18" r="3"/><circle cx="15" cy="26" r="3"/><circle cx="25" cy="26" r="3"/></g></svg>
      <span class="label">Medication Blister Packing, Daily Medication Witnessing,<br>Home Monitoring</span>
    </div>
    <div class="service" style="top:206px">
      <svg class="icon" viewBox="0 0 40 36"><path d="M3 12h34c0 10-7 17-17 17S3 22 3 12z" fill="#f15a24"/><rect x="24" y="2" width="5" height="14" rx="2" transform="rotate(30 26 9)" fill="#f15a24"/><text x="14" y="24" font-size="10" fill="#fff" font-family="Arimo, sans-serif" font-weight="700">Rx</text></svg>
      <span class="label">Customized Medications (made easy to swallow)</span>
    </div>
    <div class="service" style="top:245px">
      <svg class="icon" viewBox="0 0 40 36"><rect x="12" y="2" width="14" height="32" rx="4" fill="#f15a24" transform="rotate(-20 19 18)"/><rect x="13" y="11" width="12" height="4" fill="#fff" transform="rotate(-20 19 18)"/></svg>
      <span class="label">Custom Osteoarthritis Braces (knee, fingers, joints)</span>
    </div>
    <div class="service" style="top:284px">
      <svg class="icon" viewBox="0 0 40 36"><path d="M10 4l8 0 0 16 10 8-5 6-13-10z" fill="#f15a24" transform="rotate(-25 18 18)"/></svg>
      <span class="label">Custom Compression Socks, Lymphedema Garments,<br>Hip Protectors</span>
    </div>
    <div class="service" style="top:344px">
      <svg class="icon" viewBox="0 0 40 36"><circle cx="20" cy="7" r="5" fill="#f15a24"/><path d="M9 34V22c0-6 5-9 11-9s11 3 11 9v12z" fill="#f15a24"/><circle cx="20" cy="25" r="4" fill="none" stroke="#fff" stroke-width="2"/></svg>
      <span class="label">Ostomy, Continence, Hernia, Groin Supports</span>
    </div>
    <div class="service" style="top:382px">
      <svg class="icon" viewBox="0 0 40 36"><rect x="5" y="8" width="30" height="24" rx="3" fill="#f15a24"/><rect x="14" y="3" width="12" height="7" rx="2" fill="none" stroke="#f15a24" stroke-width="3"/><path d="M17 14h6v4h4v6h-4v4h-6v-4h-4v-6h4z" fill="#fff"/></svg>
      <span class="label">Wound Care, Specialty Dressings (wounds, burns,<br>pressure ulcers)</span>
    </div>
    <div class="service" style="top:442px">
      <svg class="icon" viewBox="0 0 40 36"><circle cx="18" cy="24" r="9" fill="none" stroke="#f15a24" stroke-width="3"/><path d="M8 4v14h18l4 14" fill="none" stroke="#f15a24" stroke-width="3"/></svg>
      <div class="label">Medical &amp; Rehab Equipment
        <ul class="sub-list">
          <li><svg class="tick" viewBox="0 0 18 18"><path d="M2 10l5 5L16 2" fill="none" stroke="#f15a24" stroke-width="3"/></svg>Sale, Rent, Installation</li>
          <li><svg class="tick" viewBox="0 0 18 18"><path d="M2 10l5 5L16 2" fill="none" stroke="#f15a24" stroke-width="3"/></svg>Home Assessment, Payment Plans, Rent to Buy</li>
        </ul>
      </div>
    </div>
    <div class="service" style="top:534px">
      <svg class="icon" viewBox="0 0 40 36"><rect x="8" y="14" width="24" height="8" rx="2" fill="#f15a24" transform="rotate(-40 20 18)"/><path d="M28 4l6 6M6 30l6-6" stroke="#f15a24" stroke-width="3"/></svg>
      <span class="label">Flu Shots, Immunizations, Vaccinations</span>
    </div>

    <p class="more-title">And that’s not all…</p>

    <div class="extra" style="top:616px">
      <div class="thumb" role="img" aria-label="Photo of a pharmacist reviewing paperwork with a senior" style="background:linear-gradient(90deg,#f2ede6,#c9d6e6)"></div>
      <span class="label">Direct Billing to Minimize Out of Pocket Expenses</span>
    </div>
    <div class="extra" style="top:687px">
      <div class="thumb" role="img" aria-label="Photo of a caregiver comforting an elderly patient" style="background:linear-gradient(90deg,#dfe6ee,#a9bccf)"></div>
      <span class="label">Multilingual Services. Specialists in Refugee &amp;<br>New Immigrant Services</span>
    </div>
    <div class="extra" style="top:754px">
      <div class="thumb" role="img" aria-label="Photo of a smiling pharmacist holding a tablet" style="background:linear-gradient(90deg,#f4f4f4,#dcdde0)"></div>
      <span class="label">Referrals accepted 7 days/wk. 24/7 On-Call Pharmacist</span>
    </div>
    <div class="extra" style="top:824px">
      <div class="thumb" role="img" aria-label="Photo of a hand holding a prescription bottle" style="background:linear-gradient(90deg,#6f7f95,#c9d0d8)"></div>
      <span class="label">Free SAME DAY Delivery</span>
    </div>
  </section>

  <section class="house-calls">
    <div class="hero" role="img" aria-label="Photo of a caregiver visiting a senior woman at home"></div>
    <h2 class="hc-title">PHARMACY MAKES HOUSE CALLS!</h2>
    <p class="hc-program">The Pharmacy at Home Program</p>
    <p class="hc-freq">Daily/Weekly/ Monthly Monitoring – <em>No Extra Costs*</em></p>

    <div class="step" style="top:296px;height:58px">
      <svg class="icon" viewBox="0 0 46 40"><path d="M4 20L23 4l19 16h-5v16H28V26h-10v10H9V20z" fill="#f15a24"/></svg>
      <span class="label">Our Pharmacist completes a medication review in<br>your home</span>
    </div>
    <div class="step" style="top:354px;height:58px">
      <svg class="icon" viewBox="0 0 46 40"><circle cx="22" cy="20" r="17" fill="none" stroke="#f15a24" stroke-width="3"/><rect x="13" y="15" width="18" height="10" rx="5" fill="#f15a24" transform="rotate(-40 22 20)"/><path d="M10 8l24 24" stroke="#f15a24" stroke-width="3"/></svg>
      <span class="label">Expired &amp; discontinued medications are removed</span>
    </div>
    <div class="step" style="top:412px;height:54px">
      <svg class="icon" viewBox="0 0 46 40"><rect x="2" y="22" width="42" height="12" fill="#f15a24"/><g fill="#f15a24"><circle cx="10" cy="16" r="3"/><circle cx="20" cy="13" r="3"/><circle cx="30" cy="16" r="3"/><rect x="34" y="8" width="8" height="4" rx="2"/></g><text x="4" y="31" font-size="7" fill="#fff" font-family="Arimo, sans-serif" letter-spacing="1.5">SMTWTFS</text></svg>
      <span class="label">Your medications are organized in daily/weekly/<br>monthly compliance cards</span>
    </div>
    <div class="step plain" style="top:466px;height:58px">
      <svg class="icon" viewBox="0 0 46 40"><rect x="10" y="3" width="24" height="32" rx="2" fill="none" stroke="#f15a24" stroke-width="2.5"/><rect x="14" y="8" width="7" height="6" fill="#f15a24"/><path d="M24 10h6M15 19h15M15 24h15M15 29h10" stroke="#f15a24" stroke-width="2"/></svg>
      <span class="label">A Medication Administration Record (MAR) is set up<br>to monitor medication compliance &amp; diagnostic tests</span>
    </div>

    <p class="daily-title">We offer DAILY SERVICES for</p>
    <ul class="daily-list">
      <li><svg class="tick" viewBox="0 0 18 18"><path d="M2 10l5 5L16 2" fill="none" stroke="#f15a24" stroke-width="3"/></svg>Medication administration &amp; ingestion witnessing</li>
      <li><svg class="tick" viewBox="0 0 18 18"><path d="M2 10l5 5L16 2" fill="none" stroke="#f15a24" stroke-width="3"/></svg>Blood pressure &amp; blood glucose monitoring, insulin administration</li>
      <li><svg class="tick" viewBox="0 0 18 18"><path d="M2 10l5 5L16 2" fill="none" stroke="#f15a24" stroke-width="3"/></svg>Transdermal patch application &amp; removal</li>
    </ul>

    <div class="step" style="top:640px;height:44px">
      <svg class="icon" viewBox="0 0 46 40"><path d="M6 14h34c0 10-7 17-17 17S6 24 6 14z" fill="#f15a24"/><rect x="27" y="3" width="5" height="14" rx="2" transform="rotate(30 29 10)" fill="#f15a24"/><text x="17" y="26" font-size="10" fill="#fff" font-family="Arimo, sans-serif" font-weight="700">Rx</text></svg>
      <span class="label">We can crush medications for easy ingestion</span>
    </div>
    <div class="step" style="top:684px;height:60px">
      <svg class="icon" viewBox="0 0 46 40"><rect x="8" y="4" width="26" height="34" rx="2" fill="none" stroke="#f15a24" stroke-width="2.5"/><path d="M12 12l3 3 4-5M12 20l3 3 4-5M12 29h4" stroke="#f15a24" stroke-width="2" fill="none"/><path d="M22 13h8M22 21h8M20 29h6M30 36l10-14" stroke="#f15a24" stroke-width="2.5"/></svg>
      <span class="label">We apply for special authority coverage on non benefit<br>medications</span>
    </div>
    <div class="step" style="top:744px;height:58px">
      <svg class="icon" viewBox="0 0 46 40"><path d="M18 4h8l4 10-4 16h-8l-3-16z" fill="#f15a24"/><rect x="18" y="30" width="8" height="6" fill="#f15a24"/><path d="M12 10c-4 2-5 6-3 9" stroke="#f15a24" stroke-width="2" fill="none"/></svg>
      <span class="label">We assist with inhaler, nebulizer, aerochamber<br>education / administration</span>
    </div>
    <div class="step plain" style="top:802px;height:56px">
      <svg class="icon" viewBox="0 0 46 40"><g fill="#f15a24"><circle cx="23" cy="11" r="6"/><path d="M13 34c0-8 4-13 10-13s10 5 10 13z"/><circle cx="10" cy="15" r="4.5"/><path d="M2 33c0-6 3-10 8-10 2 0 3 .5 4 1-2 3-3 6-3 9z"/><circle cx="36" cy="15" r="4.5"/><path d="M44 33c0-6-3-10-8-10-2 0-3 .5-4 1 2 3 3 6 3 9z"/></g></svg>
      <span class="label">We coordinate refills, follow-up with your doctor(s) &amp;<br>family, utilizing Telehealth as needed</span>
    </div>
    <p class="footnote">*No extra cost with CareCover coverage</p>
  </section>
</div>
</body>
</html>
```